Kestrel Building Works Business Card and more!

We need a business card design for Kestrel Building Works Ltd, a respected building company that specialises in high quality designer homes.

We're after a sleek, clean, modern business card that incorporates our new logo (see attached) and colours, with black being the background.

We are Certified Framing Guild and need to include their logo (see attached) on our cards, balancing but not taking over our logo.

Details to be included:

Malcolm Tivey
Director

Phone: 0218845126
Email: kestrelbuild.nz@maildrop-example.co.nz
Website: www.kestrelbuildingworks-example.co.nz

Additional Information

A start up website is also under construction and needing attention and letterheads are needed!

We look forward to your designs!

Target Market(s)

30+ people who are interested in building new or renovating current homes

Industry/Entity Type

Construction

Contact Information for Business Card

Malcolm Tivey
Director

Phone: 0218845126
Facebook: www.socialpage-example.com/kestrelbuild.nz

Font styles to use
Serif

Colors

Designer to choose colors to be used in the design.

Requirements
Must have
• Our new logo
• Our colours
• cfg logo

```html
<!DOCTYPE html>
<html lang="en">
<head>
<meta charset="utf-8">
<title>Kestrel Building Works — Business Card</title>
<link href="https://fonts.googleapis.com/css2?family=EB+Garamond:wght@400;600&display=swap" rel="stylesheet">
<style>
  :root {
    --page-bg: #3a2f2a;
    --card-black: #242424;
    --card-navy: #1d3553;
    --ink-grey: #5c5c5c;
    --ink-silver: #8a8a8a;
    --ink-white: #f2f2f2;
    --ink-gold: #d8a86b;
    --badge-white: #ffffff;
  }
  * { margin: 0; padding: 0; box-sizing: border-box; }
  html, body {
    width: 1200px; height: 715px; overflow: hidden;
    background: var(--page-bg);
    font-family: "EB Garamond", Georgia, serif;
  }
  .canvas {
    position: relative; width: 1200px; height: 715px;
    display: flex; align-items: center; justify-content: center; gap: 40px;
  }
  .card {
    position: relative; width: 540px; height: 309px;
    box-shadow: 0 12px 30px rgba(0,0,0,.45);
    overflow: hidden;
  }
  .card--front { background: var(--card-black); }
  .card--back { background: var(--card-navy); }

  .wordmark {
    position: absolute; left: 0; right: 0;
    display: flex; align-items: center; justify-content: center; gap: 10px;
    font-weight: 400; text-transform: uppercase; white-space: nowrap;
  }
  .wordmark__square { flex: none; width: 12px; height: 12px; }
  .wordmark__name { line-height: 1; }

  .card--front .wordmark { top: 116px; }
  .card--front .wordmark__name { color: var(--ink-grey); font-size: 24px; letter-spacing: 3px; }
  .card--front .wordmark__square { background: var(--ink-grey); }
  .front-website {
    position: absolute; left: 0; right: 0; bottom: 56px; text-align: center;
    font-size: 13px; letter-spacing: .3px; color: var(--ink-silver);
  }

  .card--back .wordmark { top: 88px; left: 170px; right: 20px; gap: 8px; }
  .card--back .wordmark__name { color: var(--ink-white); font-size: 18px; letter-spacing: 2.5px; }
  .card--back .wordmark__square { background: var(--ink-gold); width: 10px; height: 10px; }

  .contact { position: absolute; left: 40px; top: 150px; color: var(--ink-white); }
  .contact__name { font-size: 19px; font-weight: 600; color: var(--ink-gold); line-height: 1; }
  .contact__role { font-size: 12px; margin-top: 3px; }
  .contact__list { list-style: none; margin-top: 14px; font-size: 13px; }
  .contact__list li { display: flex; align-items: center; gap: 10px; margin-bottom: 7px; }
  .contact__icon { width: 13px; height: 13px; fill: var(--ink-white); }

  .guild-badge {
    position: absolute; right: 26px; bottom: 24px;
    width: 62px; height: 62px; border-radius: 10px; background: var(--badge-white);
  }
  .guild-badge__inner {
    position: absolute; inset: 8px; border-radius: 50%; background: #1a1a1a;
  }
</style>
</head>
<body>
<main class="canvas">
  <section class="card card--front" aria-label="Card front">
    <div class="wordmark">
      <span class="wordmark__square"></span>
      <span class="wordmark__name">Kestrel Building Works</span>
    </div>
    <p class="front-website">www.kestrelbuildingworks-example.co.nz</p>
  </section>

  <section class="card card--back" aria-label="Card back">
    <div class="wordmark">
      <span class="wordmark__square"></span>
      <span class="wordmark__name">Kestrel Building Works</span>
    </div>
    <div class="contact">
      <p class="contact__name">Malcolm Tivey</p>
      <p class="contact__role">Director</p>
      <ul class="contact__list">
        <li>
          <svg class="contact__icon" viewBox="0 0 16 16" aria-hidden="true"><path d="M3 1h3l1 4-2 1c1 2 3 4 5 5l1-2 4 1v3c0 1-1 2-2 2C7 15 1 9 1 3c0-1 1-2 2-2z"/></svg>
          <span>0218845126</span>
        </li>
        <li>
          <svg class="contact__icon" viewBox="0 0 16 16" aria-hidden="true"><path d="M1 3h14v10H1z M2 4v1l6 4 6-4V4L8 8z" fill-rule="evenodd"/></svg>
          <span>kestrelbuild.nz@maildrop-example.co.nz</span>
        </li>
      </ul>
    </div>
    <div class="guild-badge" role="img" aria-label="Certified Framing Guild badge">
      <div class="guild-badge__inner"></div>
    </div>
  </section>
</main>
</body>
</html>
```